Newspaper Ad

Please create an ad for a newspaper that is 10.5 wide and 13 inches long. Please highlight the features of the property and ensure that the name of our firm (Birchwood Hollow Estates) is the same size as our phone number which is 717-390-5168.

Pembrook's Landing and The residences at 9 N. Fern
9 N. Fern Street, Ashgrove VT

Now leasing 1, 2 & 3 bedroom units available this spring. Newley renovated apartments with stainless appliances, hardwood floors, granite countertops, in unit laundry. Includes water, sewer trash and off street parking. 1200sq first floor retail available.

717.390.5168 or www.BirchwoodHollowEstates.example for details.

```html
<!DOCTYPE html>
<html lang="en">
<head>
<meta charset="utf-8">
<title>Now Leasing – Birchwood Hollow Estates</title>
<link rel="stylesheet" href="https://fonts.googleapis.com/css2?family=Montserrat:wght@700;800&family=Open+Sans:wght@400;700&display=swap">
<style>
  :root {
    --teal: #0e6b6b;
    --charcoal: #454545;
    --footer: #3d3d3d;
    --ink: #3a3a3a;
    --white: #ffffff;
    --backdrop: #6f6f6f;
  }
  html, body {
    margin: 0;
    width: 1200px;
    height: 707px;
    overflow: hidden;
    background: linear-gradient(135deg, #5a5a5a, var(--backdrop) 50%, #8a8a8a);
  }
  .ad {
    position: absolute;
    left: 333px;
    top: 25px;
    width: 533px;
    height: 656px;
    background: var(--white);
    overflow: hidden;
    box-shadow: 0 8px 24px rgba(0,0,0,.35);
    font-family: "Open Sans", Arial, sans-serif;
  }
  .headline {
    position: absolute;
    top: 22px; left: 0; right: 0;
    margin: 0;
    text-align: center;
    font-family: "Montserrat", Arial, sans-serif;
    font-weight: 800;
    font-size: 54px;
    line-height: 1;
    letter-spacing: -0.5px;
    color: var(--teal);
  }
  .hero-photo {
    position: absolute;
    top: 103px; left: 0;
    width: 533px; height: 283px;
    background: linear-gradient(180deg, #a9bcd3 0%, #c8d3de 35%, #8a8d88 55%, #6c6e6a 78%, #3e3e42 100%);
  }
  .firm-band {
    position: absolute;
    top: 86px; left: 53px;
    width: 426px; height: 35px;
    background: var(--charcoal);
    color: var(--white);
    font-family: "Montserrat", Arial, sans-serif;
    font-weight: 700;
    font-size: 20px;
    line-height: 35px;
    text-align: center;
    letter-spacing: 0.3px;
  }
  .detail-photo {
    position: absolute;
    top: 303px; left: 40px;
    width: 187px; height: 209px;
    background: linear-gradient(180deg, #b3c3d6 0%, #9a9d97 40%, #7b7c77 70%, #8a7a6a 100%);
  }
  .location-box {
    position: absolute;
    top: 329px; left: 250px;
    width: 248px; height: 99px;
    background: linear-gradient(180deg, var(--teal) 0 53px, var(--charcoal) 53px 100%);
    color: var(--white);
    text-align: center;
    font-weight: 700;
  }
  .location-box::after {
    content: "";
    position: absolute;
    inset: 11px 4px 4px 4px;
    border: 1px solid var(--white);
    pointer-events: none;
  }
  .location-box .pin {
    position: absolute;
    top: 2px; left: 118px;
    width: 12px; height: 14px;
    z-index: 1;
  }
  .location-name {
    position: absolute;
    top: 17px; left: 0; right: 0;
    margin: 0;
    font-size: 13px;
    line-height: 16px;
  }
  .location-address {
    position: absolute;
    top: 57px; left: 0; right: 0;
    margin: 0;
    font-size: 13px;
    line-height: 16px;
    font-style: normal;
  }
  .features {
    position: absolute;
    top: 0; left: 0;
    margin: 0; padding: 0;
    list-style: none;
  }
  .feature {
    position: absolute;
    left: 270px;
    width: 248px;
    display: flex;
    align-items: center;
  }
  .feature svg { flex: none; width: 30px; height: 30px; }
  .feature p {
    margin: 0 0 0 12px;
    font-size: 8.3px;
    line-height: 11.5px;
    color: var(--ink);
  }
  .firm-name {
    position: absolute;
    top: 526px; left: 40px;
    width: 187px;
    margin: 0;
    text-align: center;
    font-family: "Montserrat", Arial, sans-serif;
    font-weight: 800;
    font-size: 23px;
    line-height: 25px;
    color: var(--ink);
  }
  .phone {
    position: absolute;
    top: 606px; left: 40px;
    width: 187px;
    text-align: center;
    font-family: "Montserrat", Arial, sans-serif;
    font-weight: 800;
    font-size: 23px;
    line-height: 26px;
    color: var(--teal);
  }
  .footer-band {
    position: absolute;
    bottom: 0; left: 0;
    width: 533px; height: 64px;
  }
  .website {
    position: absolute;
    top: 628px; left: 280px;
    display: flex;
    align-items: center;
    gap: 5px;
    font-family: "Montserrat", Arial, sans-serif;
    font-weight: 700;
    font-size: 9.4px;
    color: var(--white);
  }
</style>
</head>
<body>
  <main class="ad">
    <div class="hero-photo" role="img" aria-label="Rendering of the renovated three-storey corner building with wraparound porch under a cloudy sky"></div>
    <h1 class="headline">NOW LEASING</h1>
    <div class="firm-band">BIRCHWOOD HOLLOW ESTATES</div>

    <div class="detail-photo" role="img" aria-label="Rendering of the corner entrance and porch of the residences"></div>

    <section class="location-box">
      <svg class="pin" viewBox="0 0 12 14" aria-hidden="true">
        <rect width="12" height="14" fill="#0e6b6b"/>
        <circle cx="6" cy="4.5" r="2.6" fill="none" stroke="#fff" stroke-width="1.2"/>
        <line x1="6" y1="7.2" x2="6" y2="11" stroke="#fff" stroke-width="1.2"/>
        <line x1="3" y1="12" x2="9" y2="12" stroke="#fff" stroke-width="1"/>
      </svg>
      <p class="location-name">Pembrook's Landing and<br>The residences at 9 N. Fern</p>
      <address class="location-address">9 N. Fern Street,<br>Ashgrove VT</address>
    </section>

    <ul class="features">
      <li class="feature" style="top:440px">
        <svg viewBox="0 0 30 30" aria-hidden="true"><circle cx="15" cy="15" r="13.5" fill="#fff" stroke="#9aa" stroke-width="1"/><path d="M9 14 L15 9 L21 14 V21 H9 Z" fill="none" stroke="#555" stroke-width="1"/><rect x="13.5" y="16" width="3" height="5" fill="none" stroke="#555" stroke-width="1"/></svg>
        <p>Now leasing 1, 2 &amp; 3 bedroom units available<br>this spring.</p>
      </li>
      <li class="feature" style="top:475px">
        <svg viewBox="0 0 30 30" aria-hidden="true"><circle cx="15" cy="15" r="13.5" fill="#fff" stroke="#9aa" stroke-width="1"/><rect x="9" y="11" width="12" height="9" fill="none" stroke="#555" stroke-width="1"/><line x1="9" y1="15.5" x2="21" y2="15.5" stroke="#555" stroke-width="1"/><circle cx="11" cy="9" r="0.8" fill="#555"/><circle cx="15" cy="9" r="0.8" fill="#555"/><circle cx="19" cy="9" r="0.8" fill="#555"/></svg>
        <p>Newley renovated apartments with<br>stainless appliances, hardwood floors, granite<br>countertops, in unit laundry.</p>
      </li>
      <li class="feature" style="top:520px">
        <svg viewBox="0 0 30 30" aria-hidden="true"><circle cx="15" cy="15" r="13.5" fill="#fff" stroke="#9aa" stroke-width="1"/><rect x="9" y="8" width="7" height="8" fill="none" stroke="#555" stroke-width="1"/><text x="10.5" y="14.5" font-size="6" font-family="Arial, sans-serif" fill="#555">P</text><rect x="13" y="17" width="9" height="5" rx="1" fill="none" stroke="#555" stroke-width="1"/></svg>
        <p>Includes water, sewer trash and off street<br>parking.</p>
      </li>
      <li class="feature" style="top:560px">
        <svg viewBox="0 0 30 30" aria-hidden="true"><circle cx="15" cy="15" r="13.5" fill="#fff" stroke="#9aa" stroke-width="1"/><rect x="9" y="12" width="12" height="9" fill="none" stroke="#555" stroke-width="1"/><path d="M8 12 L10 8 H20 L22 12" fill="none" stroke="#555" stroke-width="1"/><rect x="13" y="15" width="4" height="6" fill="none" stroke="#555" stroke-width="1"/></svg>
        <p>1200sq first floor retail available.</p>
      </li>
    </ul>

    <p class="firm-name">Birchwood<br>Hollow<br>Estates</p>
    <div class="phone">717-390-5168</div>

    <svg class="footer-band" viewBox="0 0 533 64" aria-hidden="true">
      <polygon points="236,64 258,30 268,30 246,64" fill="#0e6b6b"/>
      <polygon points="250,64 272,24 533,24 533,64" fill="#3d3d3d"/>
      <circle cx="435" cy="16" r="10" fill="#0e6b6b"/>
      <circle cx="463" cy="16" r="10" fill="#0e6b6b"/>
      <circle cx="490" cy="16" r="10" fill="#0e6b6b"/>
    </svg>
    <div class="website">
      <svg width="9" height="9" viewBox="0 0 10 10" aria-hidden="true"><circle cx="5" cy="5" r="4.2" fill="none" stroke="#fff" stroke-width="1"/><ellipse cx="5" cy="5" rx="1.8" ry="4.2" fill="none" stroke="#fff" stroke-width="0.8"/><line x1="0.8" y1="5" x2="9.2" y2="5" stroke="#fff" stroke-width="0.8"/></svg>
      <span>www.BirchwoodHollowEstates.example</span>
    </div>
  </main>
</body>
</html>
```